redesing professional certificate

Redesign our certificate to more a professional look and to make it look like a-wanna have - Best in adobe photoshop, because this template will be our basic, and we have in our education different levels, basic, upper, lower, complex, master level. I usually add a small picture to show what level they are. Or when you have a better suggestion I a gladly to hear.
We teach to physiotherapist so it has to look professional.

Target Market(s)

physiotherapist

Industry/Entity Type

Health Care

Requirements
Must have
• our logo

```html
<!DOCTYPE html>
<html lang="en">
<head>
<meta charset="utf-8">
<title>Level 1 Certificate – Tissue Flow Therapy</title>
<link href="https://fonts.googleapis.com/css2?family=Great+Vibes&family=Gelasio:ital,wght@1,600&family=Fira+Sans:ital,wght@0,400;0,600;1,400;1,600&display=swap" rel="stylesheet">
<style>
  :root {
    --navy: #0f2a45;
    --navy-deep: #142543;
    --yellow: #fcc91f;
    --blue-grey: #5b86a6;
    --ink: #1d3a5b;
    --white: #ffffff;
  }
  * { margin: 0; padding: 0; box-sizing: border-box; }
  html, body { width: 848px; height: 1200px; overflow: hidden; background: var(--white); }
  .certificate {
    position: relative; width: 848px; height: 1200px; overflow: hidden;
    font-family: "Fira Sans", sans-serif; color: var(--ink);
  }
  .shapes { position: absolute; inset: 0; }
  .brand-seal {
    position: absolute; left: 68px; top: 44px; width: 192px; height: 192px;
    border-radius: 50%; background: var(--navy); border: 4px solid #24527a;
    display: flex; align-items: center; justify-content: center; text-align: center;
  }
  .brand-seal span {
    color: var(--white); font-weight: 600; font-size: 26px; line-height: 1.1;
    letter-spacing: 1px; text-transform: uppercase;
  }
  .title {
    position: absolute; left: 352px; top: 34px;
    font-family: "Great Vibes", cursive; font-size: 118px; color: var(--white);
    line-height: 1;
  }
  .level-tag {
    position: absolute; left: 720px; top: 222px; color: var(--white);
    font-style: italic; font-weight: 600; font-size: 26px;
  }
  .level-tag b { font-size: 62px; font-weight: 600; }
  .recipient {
    position: absolute; left: 92px; top: 348px; width: 528px;
    font-family: "Gelasio", serif; font-style: italic; font-weight: 600;
    font-size: 38px; color: var(--blue-grey);
    padding-bottom: 6px; border-bottom: 1px dotted var(--yellow);
  }
  .statement { position: absolute; left: 92px; top: 408px; font-style: italic; }
  .statement p { font-size: 24px; line-height: 37px; color: var(--ink); }
  .statement .course { color: var(--yellow); font-size: 30px; }
  .statement .dates { color: var(--blue-grey); font-size: 23px; }
  .signatory { position: absolute; top: 762px; width: 203px; border-top: 1px dotted var(--yellow); padding-top: 10px; font-style: italic; }
  .signatory.left { left: 92px; }
  .signatory.right { left: 444px; }
  .signatory .name { font-size: 22px; color: var(--ink); }
  .signatory .role { font-size: 16px; color: var(--blue-grey); }
  .registration { position: absolute; left: 92px; top: 856px; font-style: italic; font-weight: 600; font-size: 19px; color: var(--blue-grey); }
  .terms { position: absolute; left: 88px; top: 904px; width: 540px; font-style: italic; font-size: 19px; line-height: 26px; color: var(--blue-grey); }
  .issuer { position: absolute; left: 466px; top: 1062px; color: var(--white); }
  .issuer .company { font-weight: 600; font-size: 22px; color: var(--yellow); }
  .issuer .address { font-size: 16px; line-height: 22px; }
  .issuer .tagline { font-size: 18px; margin-top: 14px; }
</style>
</head>
<body>
<main class="certificate">
  <svg class="shapes" width="848" height="1200" viewBox="0 0 848 1200">
    <defs>
      <linearGradient id="anatomyTone" x1="0" y1="0" x2="1" y2="1">
        <stop offset="0" stop-color="#1d4a6e"/>
        <stop offset="1" stop-color="#3f7596"/>
      </linearGradient>
      <linearGradient id="treatmentTone" x1="0" y1="0" x2="1" y2="1">
        <stop offset="0" stop-color="#d9d9d9"/>
        <stop offset="1" stop-color="#6d6d6d"/>
      </linearGradient>
    </defs>
    <polygon class="header-band" points="0,0 848,0 848,180 542,278 0,44" fill="var(--navy)"/>
    <polygon class="header-photo" role="img" aria-label="Photo of back and shoulder muscles in blue tones" points="330,0 800,0 800,195 542,278 330,190" fill="url(#anatomyTone)" opacity="0.75"/>
    <polygon class="header-stripe" points="0,44 542,278 0,72" fill="var(--yellow)"/>
    <polygon class="level-corner" points="618,258 848,180 848,345" fill="var(--yellow)"/>
    <polygon class="footer-photo" role="img" aria-label="Photo of a therapist treating a patient's arm" points="0,1000 262,1120 262,1200 0,1200" fill="url(#treatmentTone)"/>
    <polygon class="footer-stripe" points="236,1122 530,1016 548,1016 262,1132" fill="var(--yellow)"/>
    <polygon class="footer-band" points="262,1132 548,1016 848,1112 848,1200 254,1200" fill="var(--navy-deep)"/>
  </svg>

  <div class="brand-seal"><span>Tissue<br>Flow</span></div>
  <h1 class="title">Certificate</h1>
  <div class="level-tag">Level <b>1</b></div>

  <div class="recipient">Daniel Moreau</div>
  <div class="statement">
    <p>has completed the fasciatherapy</p>
    <p><span class="course">Level 1 course</span> <span class="dates">-3 days, 15-17 february 2020</span></p>
    <p>at Reykjavik, Iceland 17 february 2020.</p>
  </div>

  <div class="signatory left"><div class="name">Mr. JT Holm</div><div class="role">Co-Director</div></div>
  <div class="signatory right"><div class="name">Mr. RP Senna</div><div class="role">Co-Director</div></div>

  <div class="registration">Registration number: 1 ICE 20</div>
  <p class="terms">The Tissue Flow Therapy ongoing certification is contingent upon meeting the requirements of the maintenance of the certification of Fasciatherapy</p>

  <div class="issuer">
    <div class="company">Tissueworks BV</div>
    <div class="address">Lindenstraat 14<br>3012KL Rotterdam, The Netherlands</div>
    <div class="tagline">Specialists in fasciatherapy innovation</div>
  </div>
</main>
</body>
</html>
```